Business Card Design Project

New business card design front and back for IT company that does network support and web design.
Calloway IT
Doug Calloway
Managing Director
PO Box 918 Brinsley VIC 3421
doug@callowayit.example
www.callowayit.example

Industry/Entity Type

Business

```html
<!DOCTYPE html>
<html lang="en">
<head>
<meta charset="utf-8">
<title>Calloway IT — Business Card Front</title>
<link rel="stylesheet" href="https://fonts.googleapis.com/css2?family=Didact+Gothic&display=swap">
<style>
  :root {
    --card-black: #141414;
    --card-charcoal: #262626;
    --deep-black: #050505;
    --brand-yellow: #fdc512;
    --logo-orange: #f0a04a;
    --text-white: #ffffff;
  }
  * { margin: 0; padding: 0; box-sizing: border-box; }
  html, body {
    width: 1200px;
    height: 741px;
    overflow: hidden;
    background: var(--card-black);
  }
  .card {
    position: relative;
    width: 1200px;
    height: 741px;
    overflow: hidden;
    font-family: "Didact Gothic", "Century Gothic", sans-serif;
  }
  .card-texture {
    position: absolute;
    inset: 0;
    background: radial-gradient(ellipse at 40% 40%, var(--card-charcoal) 0%, var(--card-black) 75%);
  }
  .corner-sweep {
    position: absolute;
    inset: 0;
  }
  .web-address {
    position: absolute;
    top: 36px;
    right: 24px;
    display: flex;
    align-items: center;
    gap: 12px;
    color: var(--brand-yellow);
    font-size: 33px;
    line-height: 1;
  }
  .web-address-dot {
    width: 36px;
    height: 36px;
    border-radius: 50%;
    background: var(--logo-orange);
  }
  .accent-rule {
    position: absolute;
    left: 0;
    top: 233px;
    width: 647px;
    height: 17px;
    background: var(--deep-black);
  }
  .name-band {
    position: absolute;
    left: 0;
    top: 250px;
    width: 1200px;
    height: 180px;
    background: var(--brand-yellow);
  }
  .company-name {
    position: absolute;
    left: 62px;
    top: 46px;
    color: var(--text-white);
    font-size: 82px;
    font-weight: 400;
    line-height: 1;
    letter-spacing: 1px;
  }
  .tagline {
    position: absolute;
    left: 62px;
    top: 496px;
    color: var(--brand-yellow);
    font-size: 55px;
    font-weight: 400;
    line-height: 1;
    letter-spacing: 0.5px;
  }
</style>
</head>
<body>
  <main class="card">
    <div class="card-texture" role="img" aria-label="Dark mottled charcoal texture background"></div>

    <svg class="corner-sweep" width="1200" height="741" viewBox="0 0 1200 741" aria-hidden="true">
      <path d="M1200 546 Q 820 640 454 741 L1200 741 Z" fill="var(--deep-black)"/>
    </svg>

    <div class="web-address">
      <span class="web-address-dot" aria-hidden="true"></span>
      <span>www.callowayit.example</span>
    </div>

    <div class="accent-rule"></div>

    <section class="name-band">
      <h1 class="company-name">Calloway IT</h1>
    </section>

    <p class="tagline">IT Solutions For Your Business</p>
  </main>
</body>
</html>
```